Business Cards using attached files

Please make new business cards using files attached. I would like something a little more updated possibly. Double sided.
I am wanting to make sure I can change the names and positions easily myself.

Target Market(s)

Automotive Repair

Industry/Entity Type

Automotive

Contact Information for Business Card

See attached files

Font styles to use
Serif

Colors
0054AA
0677BA
7BADD7
CADEEF
E8F1F8

Requirements
Must have
• Red white blue colors
Nice to have
• I'd like it slightly updated from our existing design. Double sided. I'd like to be able to change names and positions easily to have them printed.
Should not have
• I'm not sure

```html
<!DOCTYPE html>
<html lang="en">
<head>
<meta charset="utf-8">
<title>Harbor Auto – Business Cards</title>
<link href="https://fonts.googleapis.com/css2?family=Tinos:wght@400;700&display=swap" rel="stylesheet">
<style>
  :root {
    --navy: #1f3a5c;
    --red: #c5262e;
    --ink: #2a2f36;
    --card: #ffffff;
    --card-shade: #eef0f2;
    --backdrop: #2c2d2f;
  }
  * { box-sizing: border-box; margin: 0; padding: 0; }
  html, body { width: 1200px; height: 900px; overflow: hidden; }
  body {
    background: var(--backdrop);
    font-family: "Tinos", "Times New Roman", serif;
    color: var(--ink);
    position: relative;
  }
  .card {
    position: absolute;
    width: 700px;
    height: 400px;
    border-radius: 34px;
    background: linear-gradient(135deg, var(--card) 0%, var(--card-shade) 55%, var(--card) 100%);
    box-shadow: 0 18px 40px rgba(0,0,0,.45);
    overflow: hidden;
  }
  .card--back { left: 110px; top: 35px; }
  .card--front { left: 390px; top: 465px; }

  /* brand name */
  .brand {
    position: absolute;
    display: flex;
    align-items: center;
    gap: 12px;
    font-weight: 700;
    color: var(--navy);
    white-space: nowrap;
  }
  .brand__dot { border-radius: 50%; background: var(--red); flex: none; }
  .card--back .brand { right: 44px; top: 52px; font-size: 38px; }
  .card--back .brand__dot { width: 18px; height: 18px; }
  .card--front .brand { left: 52px; top: 118px; font-size: 48px; }
  .card--front .brand__dot { width: 22px; height: 22px; }

  /* back side */
  .service { position: absolute; left: 40px; top: 38px; }
  .heading { color: var(--red); font-weight: 700; font-size: 20px; margin-bottom: 6px; }
  .perks { list-style: none; font-size: 16.5px; line-height: 1.38; }
  .perks li { display: flex; align-items: center; gap: 10px; }
  .perks li::before {
    content: ""; width: 10px; height: 10px; border-radius: 50%;
    background: var(--navy); flex: none;
  }
  .online { margin-top: 12px; }
  .online__row { display: flex; align-items: center; gap: 10px; font-size: 16.5px; margin-top: 2px; }
  .social { display: flex; gap: 8px; margin-left: 6px; }
  .social span { width: 20px; height: 20px; border-radius: 50%; }
  .social .s1 { background: #3b5a98; }
  .social .s2 { background: #1d9bf0; }
  .social .s3 { background: #d8dade; }
  .tagline { position: absolute; left: 40px; right: 30px; bottom: 30px; font-size: 15px; line-height: 1.35; }
  .tagline strong { color: var(--navy); display: block; }
  .tagline span { color: var(--navy); font-weight: 700; }

  /* front side */
  .person { position: absolute; right: 290px; top: 250px; text-align: right; }
  .person__name { font-size: 25px; font-weight: 700; color: var(--navy); letter-spacing: .5px; text-transform: uppercase; }
  .person__role { font-size: 19px; color: #4a4f57; }
  .divider { position: absolute; left: 422px; top: 150px; width: 2px; height: 190px; background: var(--red); opacity: .75; }
  .contact { position: absolute; left: 440px; top: 150px; list-style: none; font-size: 16px; line-height: 1.55; }
  .contact li { display: flex; align-items: flex-start; gap: 8px; }
  .contact svg { width: 15px; height: 15px; margin-top: 4px; flex: none; fill: var(--navy); }
</style>
</head>
<body>

<section class="card card--back" aria-label="Card back">
  <div class="brand"><span class="brand__dot"></span>Harbor Auto</div>

  <div class="service">
    <p class="heading">We Stand Behind Our Service</p>
    <ul class="perks">
      <li>Family Owned &amp; Operated</li>
      <li>Complimentary 2 year/24,000 mile warranty</li>
      <li>Free local pickup/dropoff service</li>
      <li>Experts In Domestic &amp; Import Service</li>
      <li>Master Certified Mechanics</li>
      <li>Diesel &amp; Fleet Services Available</li>
      <li>Honest, Knowledgeable, Trustworthy Service</li>
      <li>Top-Rated A+ Auto Repair Facility</li>
    </ul>
    <div class="online">
      <p class="heading">Find Us Online:</p>
      <div class="online__row">www.harborautotruck.com
        <div class="social"><span class="s1"></span><span class="s2"></span><span class="s3"></span></div>
      </div>
    </div>
  </div>

  <p class="tagline">
    <strong>Family Owned &amp; Operated Since 1991</strong>
    <span>Auto Service - Inspections - Lube/Oil Service - Diesel - Fleet - DOT - Truck - Trailer</span>
  </p>
</section>

<section class="card card--front" aria-label="Card front">
  <div class="brand"><span class="brand__dot"></span>Harbor Auto</div>

  <div class="person">
    <p class="person__name">Daniel Corrado</p>
    <p class="person__role">General Manager</p>
  </div>

  <div class="divider"></div>

  <ul class="contact">
    <li><svg viewBox="0 0 16 16"><path d="M3 1h3l1.5 4-2 1.3a9 9 0 0 0 4.2 4.2L11 8.5l4 1.5v3a2 2 0 0 1-2 2A12 12 0 0 1 1 3a2 2 0 0 1 2-2z"/></svg>(555) 310-4821</li>
    <li><svg viewBox="0 0 16 16"><path d="M4 1h6l2 2v4H4zM2 8h12v6H2zm3 2v2h6v-2z"/></svg>(555) 310-4822</li>
    <li><svg viewBox="0 0 16 16"><path d="M1 3h14v10H1zm1.5 1.5v.4L8 9l5.5-4.1v-.4z"/></svg>dan@harborautotruck.com</li>
    <li><svg viewBox="0 0 16 16"><path d="M8 1a7 7 0 1 0 0 14A7 7 0 0 0 8 1zm0 1.6a5.4 5.4 0 0 1 0 10.8A5.4 5.4 0 0 1 8 2.6zM2.8 7.3h10.4v1.4H2.8zM7.3 2.6h1.4v10.8H7.3z"/></svg>www.harborautotruck.com</li>
    <li><svg viewBox="0 0 16 16"><path d="M8 0a5 5 0 0 0-5 5c0 4 5 11 5 11s5-7 5-11a5 5 0 0 0-5-5zm0 3a2 2 0 1 1 0 4 2 2 0 0 1 0-4z"/></svg>48 Mill Pond Road<br>Westbrook, NY 11900</li>
  </ul>
</section>

</body>
</html>
```